Design a fresh new presentation folder for us!

We are looking for a fresh design of our new presentation folder.<br/><br/>We would like our current logo and colours being used in the design as well as images associated with our industry being international logistics.<br/><br/>Our services include, international freight - sea and air, domestic road transport, 3pl and warehousing.<br/><br/>We will attach our logo and other images we have used in the past to give you an idea of what we are after. Also attached our old folder.<br/><br/>We want a brand new fresh approach that is a really modern design. It needs to be visually striking.

Industry/Entity Type

Logistic

Colors
9ccb3b
acd037
cadf82
eef4d8

Requirements
Must have
• Fresh. Modern. Visually striking. Industry related.
• Slogan - Local Knowledge, Global Strength or Complete Logistics Solutions

```html
<!DOCTYPE html>
<html lang="en">
<head>
<meta charset="utf-8">
<title>Quorvane Delivery Service – Presentation Folder</title>
<link href="https://fonts.googleapis.com/css2?family=Montserrat:wght@400;500;600;700&family=Roboto+Condensed:wght@700&display=swap" rel="stylesheet">
<style>
  :root {
    --green: #8cc43e;
    --green-light: #9ccb3b;
    --green-pale: #eef4d8;
    --grey: #58595b;
    --grey-dark: #4a4b4d;
    --white: #ffffff;
    --paper: #f4f4f3;
    --ink: #3a3b3d;
    --stage: #ecebe9;
  }
  html, body {
    margin: 0;
    width: 1200px;
    height: 2400px;
    overflow: hidden;
    background: var(--stage);
  }
  .canvas { position: relative; width: 1200px; height: 2400px; }
  .folder-outer, .folder-inner { position: absolute; display: block; }
  .folder-outer { left: 0; top: 240px; width: 1200px; height: 864px; }
  .folder-inner { left: 20px; top: 1300px; width: 1160px; height: 760px; }
  .brand-name { font: 700 27px "Montserrat", sans-serif; fill: var(--green); }
  .headline { font: 700 35px "Roboto Condensed", sans-serif; letter-spacing: 0.5px; }
  .headline-dark { fill: var(--ink); }
  .headline-green { fill: var(--green); }
  .tagline { font: 600 15px "Montserrat", sans-serif; fill: var(--ink); letter-spacing: 0.6px; }
  .web { font: 700 15px "Montserrat", sans-serif; fill: var(--ink); letter-spacing: 2px; }
  .web-accent { fill: var(--green); }
  .contact { font: 400 15px "Montserrat", sans-serif; fill: var(--white); }
</style>
</head>
<body>
<main class="canvas">

  <!-- Outside of the folder, flat die-cut -->
  <svg class="folder-outer" viewBox="100 1745 1090 785" xmlns="http://www.w3.org/2000/svg" aria-label="Folder outside, flat layout">
    <defs>
      <linearGradient id="hero-fade" x1="0" y1="0" x2="0" y2="1">
        <stop offset="0" stop-color="#ececec"/>
        <stop offset="1" stop-color="#fafafa"/>
      </linearGradient>
      <linearGradient id="panel-tint" x1="0" y1="0" x2="1" y2="0">
        <stop offset="0.5" stop-color="#ffffff"/>
        <stop offset="1" stop-color="var(--green-pale)"/>
      </linearGradient>
      <filter id="die-shadow" x="-5%" y="-5%" width="110%" height="115%">
        <feDropShadow dx="0" dy="6" stdDeviation="8" flood-color="#000" flood-opacity="0.18"/>
      </filter>
    </defs>

    <!-- die shape base (green) -->
    <path class="die-base" filter="url(#die-shadow)" fill="var(--green)"
      d="M137 1770 H1118 V2130 H1165 V2300 L1118 2320 V2505 H735 L728 2313 H710 L703 2505 H305 V2313 H137 a12 12 0 0 1 -12 -12 V1782 a12 12 0 0 1 12 -12 Z"/>

    <!-- grey field left and lower pocket -->
    <path class="grey-field" fill="var(--grey)"
      d="M137 1770 H398 L300 2120 H625 L520 2505 H305 V2313 H137 a12 12 0 0 1 -12 -12 V1782 a12 12 0 0 1 12 -12 Z"/>
    <polyline class="divider" points="398,1770 300,2120 625,2120 520,2505" fill="none" stroke="var(--white)" stroke-width="5"/>

    <!-- white content panel -->
    <path class="content-panel" fill="url(#panel-tint)"
      d="M440 1806 H1030 a45 45 0 0 1 45 45 V2230 a45 45 0 0 1 -45 45 H655 L695 2124 H357 Z"/>
    <!-- inner green stripe -->
    <polygon class="stripe" points="386,1810 440,1810 357,2118 304,2118" fill="var(--green)"/>

    <!-- industry image area -->
    <rect class="hero-image" role="img" aria-label="Faded photo of a globe, delivery trucks and stacked cargo boxes"
      x="410" y="1845" width="265" height="215" rx="6" fill="url(#hero-fade)"/>

    <!-- accreditation badges -->
    <g class="badges" fill="#c9ccd2">
      <rect x="392" y="2078" width="48" height="26" rx="4"/>
      <circle cx="475" cy="2090" r="15"/>
      <rect x="516" y="2078" width="46" height="26" rx="4"/>
      <rect x="584" y="2078" width="74" height="26" rx="4"/>
    </g>

    <!-- brand -->
    <rect x="745" y="1880" width="22" height="22" fill="var(--green)"/>
    <text class="brand-name" x="778" y="1901">Quorvane</text>

    <text class="headline headline-dark" x="743" y="2040">LOCAL KNOWLEDGE</text>
    <text class="headline headline-green" x="743" y="2076">GLOBAL STRENGTH</text>
    <rect x="745" y="2094" width="114" height="3" fill="var(--ink)"/>
    <text class="tagline" x="745" y="2132">A WORD OF EXPERIENCE AT</text>
    <text class="tagline" x="745" y="2152">YOUR FINGERTIPS</text>
    <text class="web" x="743" y="2250">www.<tspan class="web-accent">quorvane</tspan>.com</text>

    <!-- contact block -->
    <g class="contact-icons" fill="var(--green)">
      <circle cx="360" cy="2165" r="9"/>
      <circle cx="360" cy="2223" r="9"/>
      <circle cx="360" cy="2246" r="9"/>
    </g>
    <g fill="none" stroke="var(--white)" stroke-width="1.6">
      <path d="M360 2171 c-3-4-5-6-5-8 a5 5 0 0 1 10 0 c0 2-2 4-5 8 z"/>
      <rect x="357" y="2218" width="6" height="10" rx="1"/>
      <rect x="355.5" y="2243" width="9" height="6" rx="1"/>
      <rect x="357.5" y="2240" width="5" height="3"/>
    </g>
    <text class="contact" x="376" y="2170">48 Harbour Way,</text>
    <text class="contact" x="376" y="2188">Kingsford, NSW 2032,</text>
    <text class="contact" x="376" y="2206">Australia</text>
    <text class="contact" x="376" y="2228">+61 2 5550 1234</text>
    <text class="contact" x="376" y="2251">+61 2 5550 5678</text>
  </svg>

  <!-- Inside of the folder, flat spread -->
  <svg class="folder-inner" viewBox="-60 0 1160 760" xmlns="http://www.w3.org/2000/svg" aria-label="Folder inside, flat layout">
    <defs>
      <filter id="spread-shadow" x="-5%" y="-5%" width="110%" height="115%">
        <feDropShadow dx="0" dy="6" stdDeviation="8" flood-color="#000" flood-opacity="0.15"/>
      </filter>
    </defs>
    <!-- pages -->
    <rect class="page" x="0" y="60" width="1040" height="640" fill="var(--paper)" filter="url(#spread-shadow)"/>
    <line class="spine" x1="520" y1="60" x2="520" y2="700" stroke="#dcdcdc" stroke-width="2"/>
    <!-- left tab -->
    <polygon class="tab-left" points="0,330 -45,345 -45,480 0,495" fill="var(--green)"/>
    <!-- left pocket -->
    <path class="pocket-left" fill="var(--green)" d="M0 520 Q250 480 440 445 L520 560 V700 H0 Z"/>
    <path d="M0 520 Q250 480 440 445 L520 560" fill="none" stroke="var(--white)" stroke-width="4"/>
    <!-- right pocket -->
    <polygon class="pocket-right-green" points="520,520 740,505 740,700 520,700" fill="var(--green)"/>
    <polygon class="pocket-right-grey" points="748,505 1040,480 1040,700 748,700" fill="var(--grey-dark)"/>
    <line x1="744" y1="505" x2="744" y2="700" stroke="var(--white)" stroke-width="6"/>
    <!-- right flap -->
    <polygon class="flap-right" points="950,60 1040,60 1040,560 970,540" fill="var(--grey)"/>
  </svg>

</main>
</body>
</html>
```